Web Design for High End Baby Products Gear

We have some work from a designer that just didn't meet standards despite weeks of back and forth. We need someone who can come up with creative colors/fonts/etc. to make the site "pop" and give a clean, inviting feel.

We need three pages designed:

1. Home
2. Category Landing Page
3. Product Detail Page

The current site is www.HappyWheelWalks.com

Please DO NOT use current site for inspiration.

The layout should follow pretty close to what we have attached.

We were not even pleased with the logo so for now we are just concentrating on the colors and aesthetic feel of the site. You can use a nice typography type logo. We will probably have the logo done at a later time. Or if you have any ideas please feel free to submit as it may increase chances of winning design. The layout is pretty much done with the product page layout approved by our paid search people.

This is isn't where you need to spend a lot of time with general layout as it is already pretty much complete but you are free to deviate or make suggestions if you think it will help.

Reason: I haven't been able to provide adequate feedback and want to spend appropriate amount of time doing so.

I posted the set of PSD files that the previous designer completed.  We were not happy with the outcome of this.

I said in my brief "Here are a few like companies:

www.pramvault.com
www.buggynest.com
www.tiddlytopkids.com
www.kplums.com
www.wrenandtilly.com
www.doravimo.com"

What I meant was that these were similar companies to our company with respect to product/customer demographic/etc.

Reason: We have found a few that we really like and are working to determine which designs to continue with.

Thank you for your patience.

Reason: Waiting on feedback from a couple of designers so extending deadline

Thank you all.  We received several designs we really liked.  A couple stood out more than others as they seemed to hit the target on the first go around based on our brief and sample sites submitted.

There are several designers we would like to work with in the future as well as we have about 40 domains we will be developing.

Thank you.

Target Market(s)

Target Market: Female, typically 25-40 yrs old, probably married, probably career minded OR middle to upper middle income (some of our strollers are $500-$1,200), expecting mom or mom, some might have two stroller aged (double strollers). Some of our products are QUALITY (ZEK for jogging or running) or QUALITY with STYLE (Quillaro), but the truth is that this is a WANT not a need. Sure people need A stroller but not a $900 Tessel Stroller. So they have a combination of want and need coupled with ability to pay.

Brand Personality:
Definitely clean, crisp and modern. We want it to “POP” but in color and style. But I guess more directly is we want to be seen as THE or ONE of THE authorities on upper end strollers. Where you can get individual assistance, stroller consultations (yes people call in with their needs and ask advice) and personalized service as opposed to a “big box” type place that tries to be everything to everyone and when you call them you get some guy in a cubicle answering the phone that held his baby niece once. So when someone hits our site or walks into our showroom, they need to know they are in the right place.

Industry/Entity Type

Baby

Requirements
Must have
• Must a clean crisp color scheme, easy to ready, focused on products. Must instill authority, credibility, usability and be simple and uncluttered. Fonts and colors must complement each other to achieve the above.

We need three main images as well for the home page as they will be sliding/rotating images.

Backend is built in Magento so design must conform to that platform.

We retain exlusive rights to the design and all files
Nice to have
• Please see attached word file for more info.

Here are some sites we like:

www.tinyharbor.com
http://www.cubnook.com/
http://www.dapwick.com/
http://www.vemakids.com/index.php
http://www.fernwax.com/
http://www.tana-lume.com/
http://www.grelby.com/
http://www.cardsmithpartners.com/

Keep in mind that I may just like only something about the above sites and not everything. It may be color, it may be layout , font color, use of text on home page, but something about them stands out.

Here are a few like companies:

www.pramvault.com
www.buggynest.com
www.tiddlytopkids.com
www.kplums.com
www.wrenandtilly.com
www.doravimo.com
Should not have
• old dated styles, nothing "frilly"

```html
<!DOCTYPE html>
<html lang="en">
<head>
<meta charset="utf-8">
<title>Happy Wheel Walks — Home</title>
<link href="https://fonts.googleapis.com/css2?family=Josefin+Sans:wght@300;400;600&family=Lato:wght@400;700&family=Playfair+Display:wght@400&display=swap" rel="stylesheet">
<style>
:root{
  --pink:#e8457a;
  --pink-soft:#f7c6d6;
  --teal:#46afc2;
  --ink:#333;
  --muted:#777;
  --line:#dcdcdc;
  --panel:#f1f1f1;
  --page-bg:#e9e9e9;
  --footer:#1d1d1d;
  --footer-bar:#111;
  --white:#fff;
}
*{box-sizing:border-box;margin:0;padding:0}
html,body{width:1200px;height:900px;overflow:hidden}
body{background:var(--page-bg);font-family:"Lato",sans-serif;color:var(--ink);position:relative}
.backdrop{position:absolute;inset:0;background:radial-gradient(circle at 50% 40%,#f2f2f2,#dedede)}
.page{position:absolute;left:310px;top:16px;width:560px;height:884px;background:var(--white);box-shadow:0 0 6px rgba(0,0,0,.12)}
.abs{position:absolute}

/* header */
.brand-mark{left:6px;top:16px;width:40px;height:40px;border-radius:50%;background:var(--pink)}
.brand-name{left:52px;top:18px;font-family:"Playfair Display",serif;font-size:17px;line-height:18px;color:var(--pink);letter-spacing:.5px}
.promise{left:226px;top:10px;font-family:"Josefin Sans",sans-serif;font-size:10px;line-height:12px;color:var(--ink);letter-spacing:.6px}
.promise .big{font-size:17px;line-height:17px;color:var(--pink)}
.account{right:10px;top:10px;font-size:6px;color:var(--muted)}
.phone{right:10px;top:22px;font-family:"Josefin Sans",sans-serif;font-size:15px;color:var(--pink);letter-spacing:.5px}
.phone-sub{right:22px;top:38px;font-size:6px;color:var(--pink)}
.search{right:10px;top:48px;width:130px;height:12px;border:1px solid var(--line)}
.search-btn{right:10px;top:48px;width:30px;height:12px;background:var(--pink);color:#fff;font-size:6px;text-align:center;line-height:12px}

.nav{left:0;top:80px;width:560px;height:22px;border-bottom:2px solid var(--pink-soft);display:flex;align-items:center;padding-left:6px;white-space:nowrap}
.nav a{font-family:"Josefin Sans",sans-serif;font-size:8.5px;color:var(--muted);text-decoration:none;margin-right:12px;letter-spacing:.4px}
.nav a.on{color:var(--pink)}
.social{width:11px;height:11px;border-radius:2px;margin-right:4px;flex:none}
.cart{margin-left:auto;margin-right:8px;font-size:6.5px;color:var(--ink);display:flex;align-items:center;gap:4px}
.cart b{color:var(--pink);font-weight:400}

/* sidebar */
.side-box{left:4px;width:122px;background:var(--white);border:1px solid var(--line)}
.save{top:118px;height:44px;padding:6px 8px}
.save .pct{font-size:12px;color:var(--pink);font-weight:700}
.save p{font-size:6px;color:var(--muted);line-height:8px}
.shop-brand{top:168px;height:24px;padding:3px 6px;display:flex;align-items:center;gap:6px}
.shop-brand .lbl{font-size:5px;color:var(--muted);line-height:6px}
.shop-brand .lbl b{display:block;font-size:10px;color:var(--pink);font-weight:400}
.select{width:54px;height:10px;border:1px solid var(--line);font-size:5px;color:var(--muted);padding-left:2px;line-height:9px}
.cats{top:200px;height:206px;background:var(--panel);border:none;padding:6px}
.box-title{font-family:"Josefin Sans",sans-serif;font-size:5px;color:var(--muted);line-height:6px}
.box-title b{display:block;font-size:15px;color:var(--pink);font-weight:400;line-height:16px;margin-bottom:5px}
.cats ul{list-style:none;background:var(--white);padding:3px 6px}
.cats li{font-size:6.5px;color:var(--muted);line-height:8px;padding:3.5px 0;border-bottom:1px solid #eee}
.cats li:last-child{border-bottom:none}
.cats li.on{color:var(--pink)}
.refine{top:412px;height:220px;padding:8px 6px;background:var(--panel);border:none}
.refine h3{font-family:"Josefin Sans",sans-serif;font-size:14px;color:var(--pink);font-weight:400;border-bottom:1px solid var(--line);padding-bottom:5px;margin-bottom:8px}
.refine h4{font-size:6.5px;color:var(--ink);margin:8px 0 4px}
.refine li{list-style:none;font-size:6px;color:var(--muted);line-height:11px}
.refine li.on{color:var(--pink)}
.refine .more{color:var(--teal);text-decoration:underline}

/* main */
.hero{left:136px;top:114px;width:418px;height:182px;border:1px solid var(--line);overflow:hidden;background:var(--white)}
.hero-photo{position:absolute;right:0;top:0;width:270px;height:182px;background:linear-gradient(120deg,#ffffff 0%,#e6e9ea 30%,#9aa3a6 60%,#3d4447 80%,#7c8a6a 100%)}
.hero-copy{position:absolute;left:12px;top:46px}
.hero-copy h1{font-family:"Josefin Sans",sans-serif;font-weight:300;font-size:38px;line-height:34px;color:var(--teal);letter-spacing:3px}
.hero-copy h1 span{display:block;font-size:15px;line-height:17px;letter-spacing:1px;padding-left:22px;color:var(--muted)}
.hero-copy p{font-size:5.5px;color:var(--muted);width:110px;line-height:7px;margin-top:8px}
.btn{display:inline-block;background:var(--teal);color:#fff;font-size:6px;padding:3px 7px;margin-top:8px}

.tiles{left:136px;top:322px;width:418px;height:80px;display:flex;gap:4px;padding:5px;background:var(--panel)}
.tile{flex:1;background:var(--white);position:relative;border:1px solid var(--line);overflow:hidden}
.tile .ph{position:absolute;top:0;width:62px;height:68px;background:linear-gradient(150deg,#fbeee5,#e8b9a1 60%,#c98f74)}
.tile .txt{position:absolute;top:16px;width:70px;font-family:"Josefin Sans",sans-serif;color:var(--pink);font-size:11px;text-align:center;line-height:12px}
.tile .txt small{display:block;font-size:5px;color:var(--muted);margin-top:3px}
.tile .tag{display:inline-block;background:var(--pink);color:#fff;font-size:5px;padding:2px 5px;margin-top:4px;line-height:6px}

.news-row{left:136px;top:408px;width:418px;height:46px}
.news-flag{position:absolute;left:4px;top:6px;width:32px;height:32px;background:var(--teal);color:#fff;font-size:8px;font-family:"Josefin Sans",sans-serif;text-align:center;line-height:32px;transform:rotate(-35deg)}
.news-copy{position:absolute;left:46px;top:10px;width:96px;font-size:5px;color:var(--muted);line-height:7px}
.blog{position:absolute;left:152px;top:14px;display:flex;align-items:center;gap:4px;font-family:"Josefin Sans",sans-serif;font-size:14px;color:var(--ink)}
.newsletter{position:absolute;left:222px;top:4px;width:196px;height:38px;border-left:1px solid var(--line);padding-left:10px}
.newsletter h5{font-family:"Josefin Sans",sans-serif;font-weight:400;font-size:10px;color:var(--pink)}
.newsletter .field{position:absolute;left:10px;top:18px;width:150px;height:12px;border:1px solid var(--line)}
.newsletter .go{position:absolute;left:168px;top:15px;width:18px;height:18px;border-radius:50%;background:var(--pink);color:#fff;font-size:5px;text-align:center;line-height:18px}

.section-tab{left:136px;height:16px;padding:0 12px;background:linear-gradient(#ececec,#cdcdcd);font-family:"Josefin Sans",sans-serif;font-size:9px;line-height:17px;color:var(--ink)}
.section-rule{left:136px;width:418px;height:1px;background:var(--line)}
.products{left:136px;top:492px;width:418px;height:116px;display:flex;align-items:center;gap:6px}
.arrow{width:9px;height:9px;border-radius:50%;background:#bbb;flex:none}
.product{flex:1;height:112px;border:1px solid var(--line);position:relative;text-align:center}
.product .ph{position:absolute;left:12px;top:8px;right:12px;height:56px;background:linear-gradient(180deg,#ececec,#9fb5b5)}
.p2 .ph{background:linear-gradient(180deg,#f8d9e2,#d26b8c)}
.p3 .ph{background:linear-gradient(180deg,#e9e2d2,#5c7a5a)}
.p4 .ph{background:linear-gradient(180deg,#f2f2f2,#c8353e)}
.product .name{position:absolute;left:0;right:0;top:70px;font-size:5.5px;color:var(--muted)}
.product .price{position:absolute;left:0;right:0;top:78px;font-size:5.5px;color:var(--pink)}
.product .stars{position:absolute;left:0;right:0;top:85px;font-size:7px;color:var(--pink);letter-spacing:1px}
.product .stars i{color:#ccc;font-style:normal}
.product .rev{position:absolute;left:0;right:0;top:97px;font-size:5px;color:var(--muted)}
.sale-dot{position:absolute;left:4px;top:30px;width:26px;height:26px;border-radius:50%;background:var(--pink);color:#fff;font-size:6px;line-height:26px;z-index:1}

.brands{left:136px;top:678px;width:418px;height:30px;display:flex;align-items:center;justify-content:space-between;padding:0 2px}
.brands span.nm{font-size:10px;font-weight:700;color:var(--ink)}
.brands .lumo{color:var(--pink)}

/* footer */
.footer{left:0;top:728px;width:560px;height:136px;background:var(--footer);padding:10px 14px;display:flex;gap:14px}
.col{width:122px}
.col h6{font-size:7px;color:var(--pink);font-weight:700;margin-bottom:3px;margin-top:2px}
.col p{font-size:5.5px;color:#bbb;line-height:7px}
.bottom{left:0;top:864px;width:560px;height:20px;background:var(--footer-bar);color:#ccc;font-size:5.5px;display:flex;align-items:center;padding:0 10px}
.bottom .follow{margin-left:auto;display:flex;gap:3px;align-items:center}
.bottom .follow i{width:8px;height:8px;border-radius:2px;background:#4f8fd1;display:inline-block}
</style>
</head>
<body>
<div class="backdrop" role="img" aria-label="Soft grey background with faint silhouettes of toddlers"></div>

<div class="page">
  <header>
    <div class="abs brand-mark"></div>
    <div class="abs brand-name">HAPPY WHEEL<br>WALKS</div>
    <div class="abs promise">365 DAY RETURNS<br><span class="big">FREE SHIPPING</span><br>NO SALES TAX<br>PRICE MATCH GUARANTEE</div>
    <div class="abs account">Registry | Check Out | My Account</div>
    <div class="abs phone">1.800.555.0142</div>
    <div class="abs phone-sub">(800) 555-0143</div>
    <div class="abs search"></div>
    <div class="abs search-btn">Search</div>
    <nav class="abs nav">
      <a class="on">HOME</a><a>SALE</a><a>GIFT REGISTRY</a><a>GIFT CARDS</a><a>CONTACT US</a><a>STORE LOCATION</a><a>BLOG</a>
      <span class="social" style="background:#3b5b98"></span><span class="social" style="background:#4fb6e6"></span>
      <span class="cart"><svg width="10" height="9" viewBox="0 0 10 9"><path d="M0 1h2l1.5 5h5L10 2.5H3" fill="none" stroke="#555" stroke-width="1"/><circle cx="4" cy="8" r=".9" fill="#555"/><circle cx="8" cy="8" r=".9" fill="#555"/></svg>Shopping Cart <b>(0 items)</b></span>
    </nav>
  </header>

  <aside>
    <div class="abs side-box save"><div class="pct">Save 5%</div><p>when you sign up for our newsletter, it even discounts!</p></div>
    <div class="abs side-box shop-brand"><div class="lbl">SHOP BY<b>Brand</b></div><div class="select">Select a brand ▾</div></div>
    <div class="abs side-box cats">
      <div class="box-title">SHOP BY<b>Category</b></div>
      <ul>
        <li class="on">Baby Strollers (75)</li><li>Child Bike Trailers (28)</li><li>Accessories (34)</li><li>Convertible Kits (18)</li><li>Rain / Sun Covers (22)</li><li>Category 6 (15)</li><li>Category 7 Longer Line For Sample (78)</li><li>Category 8 (4)</li>
      </ul>
    </div>
    <div class="abs side-box refine">
      <h3>Refine Results</h3>
      <h4>Brand</h4>
      <ul><li class="on">Tottlerun (4)</li><li>ZEK (4)</li><li>Quillaro Cameo (1)</li><li>Tessel Lumen (2)</li><li class="more">See All Brands</li></ul>
      <h4>Best Use</h4>
      <ul><li>Casual (4)</li><li>Cross-training (4)</li><li>Cycling (4)</li><li>Running (4)</li></ul>
    </div>
  </aside>

  <main>
    <section class="abs hero">
      <div class="hero-photo" role="img" aria-label="Premium black stroller with large wheels photographed outdoors"></div>
      <div class="hero-copy">
        <h1>WALK<span>YOUR WAY</span></h1>
        <p>Lorem ipsum is simply dummy text of the printing and typesetting industry.</p>
        <span class="btn">READ MORE</span>
      </div>
    </section>

    <section class="abs tiles">
      <div class="tile"><div class="ph" style="left:0" role="img" aria-label="Parent holding a smiling baby"></div><div class="txt" style="left:62px">STARTING<br>SOLIDS<small>check it out</small></div></div>
      <div class="tile"><div class="ph" style="left:0" role="img" aria-label="Baby eating from a spoon"></div><div class="txt" style="left:62px">BABY<br>SOLIDS<br><span class="tag">Baby Registry</span></div></div>
      <div class="tile"><div class="txt" style="left:0">NEW<br>ARRIVALS<small>check it out</small></div><div class="ph" style="right:0" role="img" aria-label="Infant lying on a soft blanket"></div></div>
    </section>

    <section class="abs news-row">
      <div class="news-flag">News</div>
      <p class="news-copy">Lorem ipsum is simply dummy text of the printing and typesetting industry. Lorem ipsum has been.</p>
      <div class="blog"><svg width="10" height="12" viewBox="0 0 10 12"><path d="M0 0l10 6-10 6z" fill="#555"/></svg>Blog</div>
      <div class="newsletter"><h5>Sign Up for Our Newsletter</h5><div class="field"></div><div class="go">GO</div></div>
    </section>

    <div class="abs section-tab" style="top:462px">Featured Products</div>
    <div class="abs section-rule" style="top:478px"></div>
    <section class="abs products">
      <span class="arrow"></span>
      <div class="product p1"><span class="sale-dot">$30.00</span><div class="ph" role="img" aria-label="Teal patterned diaper bag"></div><div class="name">Name Lorem Ipsum</div><div class="price">$69.99</div><div class="stars">★★★★<i>★</i></div><div class="rev">21 Reviews</div></div>
      <div class="product p2"><div class="ph" role="img" aria-label="Pink polka dot diaper bag"></div><div class="name">Name Lorem Ipsum</div><div class="price">$69.99</div><div class="stars">★★★★<i>★</i></div><div class="rev">21 Reviews</div></div>
      <div class="product p3"><div class="ph" role="img" aria-label="Striped tote diaper bag"></div><div class="name">Name Lorem Ipsum</div><div class="price">$69.99</div><div class="stars">★★★★<i>★</i></div><div class="rev">21 Reviews</div></div>
      <div class="product p4"><div class="ph" role="img" aria-label="Red compact stroller"></div><div class="name">Name Lorem Ipsum</div><div class="price">$69.99</div><div class="stars">★★★★<i>★</i></div><div class="rev">21 Reviews</div></div>
      <span class="arrow"></span>
    </section>

    <div class="abs section-tab" style="top:634px">Featured Brands</div>
    <div class="abs section-rule" style="top:650px"></div>
    <section class="abs brands">
      <span class="arrow"></span>
      <span class="nm">Tottlerun</span><span class="nm">ZEK</span><span class="nm">Quillaro</span><span class="nm">Brisa</span><span class="nm lumo">Lumo</span><span class="nm">Vextra</span>
      <span class="arrow"></span>
    </section>
  </main>

  <footer>
    <div class="abs footer">
      <div class="col"><h6>Happy Wheel Walks</h6><p>About HWW<br>Jobs at HWW<br>100% Satisfaction<br>Guarantee<br>Corporate &amp; Group Sales<br>Privacy Policy<br>Terms of Use<br>Site Index</p></div>
      <div class="col"><h6>Become a Seller</h6><p>Become an HWW Reseller<br>Member Help<br>Find Membership Number</p><h6>More Useful Links</h6><p>Lorem Ipsum<br>Dolor Sit Amet<br>Tandem Donec</p></div>
      <div class="col"><h6>Stroller Expert</h6><p>Stroller Expert Articles<br>Lorem Ipsum Sit<br>Donec Tandem Quisque</p><h6>More Useful Links</h6><p>Lorem Ipsum<br>Dolor Sit Amet<br>Tandem Donec</p></div>
      <div class="col"><h6>Help</h6><p>Help Section<br>Contact Us<br>Live Help<br>Order Status<br>Returns &amp; Exchanges<br>Product Safety<br>Shipping Info<br>Another link</p></div>
    </div>
    <div class="abs bottom">© 2011 Happy Wheel Walks. All Rights Reserved.
      <span class="follow">For The Latest News and Special Offers, Follow Us: <i></i><i></i><i></i><i></i><i></i></span>
    </div>
  </footer>
</div>
</body>
</html>
```